The Little Sprout Gathering -Flyer Design

The flyer is for a conference that is being held for Chiropractors to gain continuing education in paediatrics with all proceeds from the event going to paediatric research.

Paediatric chiropractic is mostly about how we can help the body and brain develop optimally with a big focus of the nervous system. I have attached the logo and the website is www.littlesproutgathering.example. The feel should be kid friendly but also professional. It is also going to be largely for the American Market.

Here is an outline of the copy that we need on this flyer:
========================================
Don’t Miss This….some of the best minds in Chiropractic Pediatrics…all together in the USA.

23-24th April 2016, San Francisco. Sat 23rd 8.30-5.30 Sun 24th 8.30am -1pm

Harborline Lodge by Brennard, ​Bayview Terminal-Pierside

With all proceeds going directly to Pediatric based research projects at the Institute for Spinal Wellness Studies at QVSI.

Learn From:

Dr. Marlene Vostrik
Dr. Ilse Fenwarr
Dr. Petra Lindqvol
Dr. Rosalind Pettow
Dr. Tommy Merravin
Dr. Annabelle Throssel
Dr. Josephine Throssel
Dr. Greta Molloru
Dr. Nora Falby
Dr. Miriam Pask

Early bird $449 18th Mar 2016

CE available

More info at www.littlesproutgathering.example (could we also have a Facebook icon too!)

```html
<!DOCTYPE html>
<html lang="en">
<head>
<meta charset="utf-8">
<title>The Little Sprout Gathering – Flyer</title>
<link rel="stylesheet" href="https://fonts.googleapis.com/css2?family=Roboto+Condensed:wght@400;700&family=Open+Sans:wght@400;600;700&display=swap">
<style>
  :root {
    --orange: #ef5a24;
    --navy: #1b3252;
    --green: #6b9a2e;
    --ink: #141414;
    --white: #ffffff;
  }
  * { margin: 0; padding: 0; box-sizing: border-box; }
  html, body { width: 907px; height: 1200px; overflow: hidden; background: var(--white); }
  .flyer { position: relative; width: 907px; height: 1200px; overflow: hidden; font-family: "Open Sans", sans-serif; color: var(--ink); }
  .flyer-shapes { position: absolute; inset: 0; }
  .headline { position: absolute; left: 436px; width: 460px; text-align: center; font-family: "Roboto Condensed", sans-serif; font-weight: 700; white-space: nowrap; line-height: 1; }
  .headline-name { top: 78px; font-size: 33px; color: var(--white); }
  .headline-city { top: 132px; font-size: 31px; color: var(--white); }
  .headline-date { top: 180px; font-size: 64px; color: var(--ink); }
  .pitch { position: absolute; left: 430px; width: 450px; text-align: center; font-family: "Roboto Condensed", sans-serif; line-height: 1; white-space: nowrap; }
  .pitch-lead { top: 408px; font-size: 40px; font-weight: 700; }
  .pitch-minds { top: 458px; font-size: 33px; font-weight: 700; }
  .pitch-field { top: 506px; font-size: 30px; }
  .pitch-place { top: 552px; font-size: 34px; }
  .learn-tab { position: absolute; left: 0; top: 484px; width: 237px; height: 44px; background: var(--navy); border: 2px solid var(--white); border-left: none; border-radius: 0 22px 22px 0; color: var(--white); font-family: "Roboto Condensed", sans-serif; font-weight: 700; font-size: 23px; line-height: 40px; padding-left: 44px; }
  .speakers { position: absolute; left: 44px; top: 545px; list-style: none; }
  .speaker { display: flex; align-items: center; gap: 9px; height: 25px; color: var(--white); font-size: 17px; font-weight: 600; white-space: nowrap; }
  .speaker svg { width: 11px; height: 13px; flex: none; }
  .early-bird { position: absolute; left: 74px; top: 810px; width: 156px; height: 156px; border-radius: 50%; background: var(--white); border: 6px solid var(--orange); box-shadow: 0 0 0 3px var(--white); text-align: center; font-family: "Roboto Condensed", sans-serif; font-weight: 700; padding-top: 28px; }
  .early-bird-label { color: var(--green); font-size: 18px; line-height: 1.1; }
  .early-bird-price { color: var(--orange); font-size: 36px; line-height: 1; }
  .early-bird-date { color: var(--ink); font-size: 16px; margin-top: 3px; }
  .ce-note { position: absolute; left: 0; width: 300px; top: 986px; text-align: center; color: var(--white); font-family: "Roboto Condensed", sans-serif; font-weight: 700; font-size: 30px; line-height: 1; }
  .date-pill { position: absolute; left: 478px; top: 680px; width: 330px; height: 44px; border-radius: 22px; background: var(--navy); color: var(--white); text-align: center; font-family: "Roboto Condensed", sans-serif; font-weight: 700; font-size: 26px; line-height: 44px; }
  .details { position: absolute; left: 420px; width: 460px; text-align: center; }
  .details-times { top: 740px; font-weight: 700; font-size: 19px; }
  .details-venue { top: 778px; font-size: 19px; line-height: 28px; }
  .details-cause { top: 854px; font-size: 18px; line-height: 26px; }
  .brand { position: absolute; left: 44px; top: 1112px; display: flex; align-items: center; gap: 12px; }
  .brand-dot { width: 32px; height: 32px; border-radius: 50%; background: var(--orange); }
  .brand-name { color: var(--orange); font-family: "Roboto Condensed", sans-serif; font-weight: 700; font-size: 23px; white-space: nowrap; }
  .contact { position: absolute; right: 42px; text-align: right; font-family: "Roboto Condensed", sans-serif; font-weight: 700; white-space: nowrap; line-height: 1; }
  .contact-label { color: var(--orange); font-size: 29px; }
  .contact-value { color: var(--white); font-size: 21px; font-family: "Open Sans", sans-serif; }
  .contact-web-label { top: 1020px; }
  .contact-web { top: 1058px; }
  .contact-mail-label { top: 1100px; }
  .contact-mail { top: 1140px; }
</style>
</head>
<body>
<main class="flyer">
  <svg class="flyer-shapes" width="907" height="1200" viewBox="0 0 907 1200">
    <defs>
      <linearGradient id="mist" x1="0" y1="0" x2="0" y2="1">
        <stop offset="0" stop-color="#dcdcdc"/>
        <stop offset="0.5" stop-color="#ffffff"/>
        <stop offset="1" stop-color="#f4f4f4"/>
      </linearGradient>
      <radialGradient id="photo-tone" cx="0.45" cy="0.55" r="0.7">
        <stop offset="0" stop-color="#d9bfae"/>
        <stop offset="0.6" stop-color="#8a6d5a"/>
        <stop offset="1" stop-color="#3b2f2a"/>
      </radialGradient>
    </defs>
    <rect class="band-orange" x="0" y="0" width="907" height="430" fill="var(--orange)"/>
    <path class="band-navy" d="M0,340 C240,470 520,300 907,292 L907,520 L0,520 Z" fill="var(--navy)"/>
    <path class="panel-mist" d="M330,400 C520,320 720,318 907,322 L907,1000 L330,1000 Z" fill="url(#mist)"/>
    <path class="panel-lower" d="M310,676 C520,636 720,644 907,664 L907,1000 L310,1000 Z" fill="var(--white)"/>
    <path d="M350,660 C540,620 720,628 907,648" fill="none" stroke="var(--orange)" stroke-width="5"/>
    <path d="M520,642 C660,618 800,622 907,636" fill="none" stroke="var(--green)" stroke-width="4"/>
    <path class="column-green" d="M0,420 C150,430 290,400 386,360 C330,560 300,820 304,1060 L0,1060 Z" fill="var(--green)"/>
    <path d="M386,360 C330,560 300,820 304,1060" fill="none" stroke="var(--white)" stroke-width="10"/>
    <path d="M395,362 C340,560 312,820 316,1060" fill="none" stroke="var(--orange)" stroke-width="5"/>
    <path class="band-footer" d="M0,1044 C300,1074 600,964 907,949 L907,1200 L0,1200 Z" fill="var(--navy)"/>
    <path d="M0,1038 C300,1066 600,956 907,942" fill="none" stroke="var(--orange)" stroke-width="5"/>
    <circle cx="200" cy="180" r="232" fill="var(--white)"/>
    <circle cx="200" cy="180" r="224" fill="url(#photo-tone)" role="img" aria-label="Photo of a baby held in a parent's arms at the seminar"/>
  </svg>

  <h1 class="headline headline-name">THE LITTLE SPROUT GATHERING</h1>
  <p class="headline headline-city">IS COMING TO SAN FRANCISCO</p>
  <p class="headline headline-date">in April 2016</p>

  <p class="pitch pitch-lead">Don’t Miss This….</p>
  <p class="pitch pitch-minds">some of the best minds</p>
  <p class="pitch pitch-field">in Chiropractic Pediatrics…</p>
  <p class="pitch pitch-place">all together in the USA</p>

  <div class="learn-tab">LEARN FROM</div>
  <ul class="speakers">
    <li class="speaker"><svg viewBox="0 0 12 14"><circle cx="6" cy="4" r="3.2" fill="var(--navy)"/><path d="M0,14 C0,8 12,8 12,14 Z" fill="var(--navy)"/></svg>Dr. Marlene Vostrik</li>
    <li class="speaker"><svg viewBox="0 0 12 14"><circle cx="6" cy="4" r="3.2" fill="var(--navy)"/><path d="M0,14 C0,8 12,8 12,14 Z" fill="var(--navy)"/></svg>Dr. Ilse Fenwarr</li>
    <li class="speaker"><svg viewBox="0 0 12 14"><circle cx="6" cy="4" r="3.2" fill="var(--navy)"/><path d="M0,14 C0,8 12,8 12,14 Z" fill="var(--navy)"/></svg>Dr. Petra Lindqvol</li>
    <li class="speaker"><svg viewBox="0 0 12 14"><circle cx="6" cy="4" r="3.2" fill="var(--navy)"/><path d="M0,14 C0,8 12,8 12,14 Z" fill="var(--navy)"/></svg>Dr. Rosalind Pettow</li>
    <li class="speaker"><svg viewBox="0 0 12 14"><circle cx="6" cy="4" r="3.2" fill="var(--navy)"/><path d="M0,14 C0,8 12,8 12,14 Z" fill="var(--navy)"/></svg>Dr. Tommy Merravin</li>
    <li class="speaker"><svg viewBox="0 0 12 14"><circle cx="6" cy="4" r="3.2" fill="var(--navy)"/><path d="M0,14 C0,8 12,8 12,14 Z" fill="var(--navy)"/></svg>Dr. Annabelle Throssel</li>
    <li class="speaker"><svg viewBox="0 0 12 14"><circle cx="6" cy="4" r="3.2" fill="var(--navy)"/><path d="M0,14 C0,8 12,8 12,14 Z" fill="var(--navy)"/></svg>Dr. Josephine Throssel</li>
    <li class="speaker"><svg viewBox="0 0 12 14"><circle cx="6" cy="4" r="3.2" fill="var(--navy)"/><path d="M0,14 C0,8 12,8 12,14 Z" fill="var(--navy)"/></svg>Dr. Greta Molloru</li>
    <li class="speaker"><svg viewBox="0 0 12 14"><circle cx="6" cy="4" r="3.2" fill="var(--navy)"/><path d="M0,14 C0,8 12,8 12,14 Z" fill="var(--navy)"/></svg>Dr. Nora Falby</li>
    <li class="speaker"><svg viewBox="0 0 12 14"><circle cx="6" cy="4" r="3.2" fill="var(--navy)"/><path d="M0,14 C0,8 12,8 12,14 Z" fill="var(--navy)"/></svg>Dr. Miriam Pask</li>
  </ul>

  <div class="early-bird">
    <p class="early-bird-label">EARLY BIRD</p>
    <p class="early-bird-price">$449</p>
    <p class="early-bird-date">18th Mar 2016</p>
  </div>
  <p class="ce-note">CE available</p>

  <div class="date-pill">23-24th April 2016</div>
  <p class="details details-times">Sat 23rd 8.30-5.30 Sun 24th 8.30am -1pm</p>
  <p class="details details-venue">Harborline Lodge by Brennard<br>Bayview Terminal-Pierside</p>
  <p class="details details-cause">With all proceeds going directly to Pediatric<br>based research projects at the Institute for Spinal<br>Wellness Studies at QVSI</p>

  <div class="brand">
    <span class="brand-dot"></span>
    <span class="brand-name">The Little Sprout Gathering</span>
  </div>

  <p class="contact contact-label contact-web-label">More info at</p>
  <p class="contact contact-value contact-web">www.littlesproutgathering.example</p>
  <p class="contact contact-label contact-mail-label">email at</p>
  <p class="contact contact-value contact-mail">info@littlesproutgathering.example</p>
</main>
</body>
</html>
```